Bravo Ledger Path Tracker

Consumers track their three credit scores. I have sent an illustration after one update of their credit scores. Many consumers will have a dozen updates during one year. I would like to show a history of the last 24 months. Put together a design that is attractive and easy to look at and follow. I have updated some ideas for graphs (Apr 5, 2022)

Target Market(s)

Consumers tracking their credit scores

Coding

Coded - Design and coding required

Number of Pages Required

1 page

Colors
0054AA
0677BA
7BADD7
CADEEF
E8F1F8
00AB8E
00BBA5
67D7C9
C6EFE9
E9F9F6

Requirements
Must have
• Scores from 350 to 850 pon the left hand side - dates the credit scores were pulled at the bottom on the x axis
Nice to have
• 3 digit credit score for each of the three scores /

```html
<!DOCTYPE html>
<html lang="en">
<head>
<meta charset="utf-8">
<title>Bravo Ledger Path Tracker – Credit Score History</title>
<link rel="stylesheet" href="https://fonts.googleapis.com/css2?family=Poppins:wght@400;500;600;700&display=swap">
<style>
  :root {
    --page: #ffffff;
    --header: #081c2d;
    --overview-bg: #e8f1f8;
    --ink: #1a1f2b;
    --muted: #5f6b7a;
    --tab-active: #7badd7;
    --navy: #0054aa;
    --navy-deep: #003f82;
    --navy-mark: #0677ba;
    --teal: #00ab8e;
    --teal-deep: #008a72;
    --teal-mark: #00bba5;
    --sky: #7badd7;
    --sky-deep: #0677ba;
    --sky-mark: #0677ba;
    --sky-ink: #0a2540;
    --axis: #111;
    --tick: #b8bcc4;
  }
  * { box-sizing: border-box; margin: 0; padding: 0; }
  html, body { width: 1200px; height: 797px; overflow: hidden; background: var(--page); font-family: "Poppins", sans-serif; color: var(--ink); }
  .frame { position: absolute; left: 26px; top: 28px; width: 1148px; height: 736px; background: #fff; box-shadow: 0 2px 22px rgba(0,0,0,.12); }
  .topbar { height: 42px; background: var(--header); display: flex; align-items: center; padding-left: 89px; }
  .topbar h1 { color: #fff; font-size: 11px; font-weight: 500; letter-spacing: .1px; }
  .overview { position: relative; height: 187px; background: var(--overview-bg); }
  .overview-title { position: absolute; left: 89px; top: 15px; font-size: 14px; font-weight: 500; }
  .divider { position: absolute; left: 170px; top: 18px; width: 1px; height: 16px; background: #b9c6d3; }
  .tabs { position: absolute; left: 193px; top: 15px; display: flex; }
  .tab { font-size: 9.5px; color: var(--muted); padding: 4px 8px; border-radius: 3px; }
  .tab.active { background: var(--tab-active); color: #fff; }
  .duration { position: absolute; left: 882px; top: 15px; display: flex; align-items: center; gap: 8px; }
  .duration-label { font-size: 11px; }
  .duration-field { display: flex; height: 22px; border: 1px solid #9aa6b3; border-radius: 2px; background: #f7fafc; }
  .duration-value { font-size: 7.5px; padding: 0 10px 0 8px; display: flex; align-items: center; }
  .duration-icon { width: 29px; border-left: 1px solid #9aa6b3; display: flex; align-items: center; justify-content: center; }
  .cards { position: absolute; left: 89px; top: 53px; display: flex; gap: 9px; }
  .card { position: relative; width: 159px; height: 115px; border-radius: 4px; color: #fff; padding: 14px 17px; }
  .card.navy { background: var(--navy); }
  .card.teal { background: var(--teal); }
  .card.sky { background: var(--sky); color: var(--sky-ink); }
  .bureau-mark { position: absolute; right: 6px; top: 4px; font-size: 10px; font-weight: 500; }
  .navy .bureau-mark { color: var(--navy-mark); }
  .teal .bureau-mark { color: var(--teal-mark); }
  .sky .bureau-mark { color: var(--sky-mark); }
  .bureau-name { font-size: 11px; margin-top: 6px; }
  .score { font-size: 19px; font-weight: 700; margin-top: 9px; line-height: 1; }
  .change { position: absolute; left: 17px; top: 81px; width: 79px; height: 20px; border-radius: 10px; display: flex; align-items: center; justify-content: center; gap: 4px; font-size: 10.5px; font-weight: 500; color: #fff; }
  .navy .change { background: var(--navy-deep); }
  .teal .change { background: var(--teal-deep); }
  .sky .change { background: var(--sky-deep); }
  .chart { position: absolute; left: 0; top: 229px; }
  .chart text { font-family: "Poppins", sans-serif; }
</style>
</head>
<body>
<div class="frame">
  <header class="topbar"><h1>My Credit Score History</h1></header>

  <section class="overview">
    <h2 class="overview-title">Overview</h2>
    <span class="divider"></span>
    <nav class="tabs">
      <span class="tab">6 Months</span>
      <span class="tab active">12 Months</span>
      <span class="tab">24 Months</span>
    </nav>
    <div class="duration">
      <span class="duration-label">Duration</span>
      <div class="duration-field">
        <span class="duration-value">Jan 2021 - Dec 2021</span>
        <span class="duration-icon">
          <svg width="10" height="10" viewBox="0 0 10 10" fill="none" stroke="#333" stroke-width=".9"><rect x="1" y="1.8" width="8" height="7.4" rx="1"/><line x1="1" y1="4" x2="9" y2="4"/><line x1="3" y1=".6" x2="3" y2="2.6"/><line x1="7" y1=".6" x2="7" y2="2.6"/></svg>
        </span>
      </div>
    </div>

    <div class="cards">
      <article class="card navy">
        <span class="bureau-mark">Veridian</span>
        <p class="bureau-name">Veridian</p>
        <p class="score">750</p>
        <span class="change"><svg width="10" height="10" viewBox="0 0 10 10" fill="none" stroke="#fff" stroke-width="1.2"><path d="M2 8 8 2M3.5 2H8v4.5"/></svg>50</span>
      </article>
      <article class="card teal">
        <span class="bureau-mark">Northgate</span>
        <p class="bureau-name">Northgate</p>
        <p class="score">740</p>
        <span class="change"><svg width="10" height="10" viewBox="0 0 10 10" fill="none" stroke="#fff" stroke-width="1.2"><path d="M8 2 2 8M2 3.5V8h4.5"/></svg>10</span>
      </article>
      <article class="card sky">
        <span class="bureau-mark">Crestline</span>
        <p class="bureau-name">Crestline</p>
        <p class="score">760</p>
        <span class="change"><svg width="10" height="10" viewBox="0 0 10 10" fill="none" stroke="#fff" stroke-width="1.2"><path d="M2 8 8 2M3.5 2H8v4.5"/></svg>80</span>
      </article>
    </div>
  </section>

  <svg class="chart" width="1148" height="507" viewBox="52 505 2258 998" role="img" aria-label="Line chart of three credit scores on a 350 to 850 scale, January to December 2021">
    <g class="legend-toggle" fill="none" stroke="#b5b9c0" stroke-width="2">
      <circle cx="2265" cy="515" r="5"/><line x1="2280" y1="515" x2="2298" y2="515"/>
      <line x1="2259" y1="539" x2="2276" y2="539"/><circle cx="2292" cy="539" r="5"/>
    </g>

    <g class="y-axis" font-size="19" fill="#5f6b7a" text-anchor="end">
      <line x1="226" y1="551" x2="226" y2="1326" stroke="var(--axis)" stroke-width="2.5"/>
      <g stroke="var(--tick)" stroke-width="1.5">
        <line x1="212" y1="569" x2="242" y2="569"/><line x1="212" y1="715" x2="242" y2="715"/>
        <line x1="212" y1="861" x2="242" y2="861"/><line x1="212" y1="1008" x2="242" y2="1008"/>
        <line x1="212" y1="1154" x2="242" y2="1154"/><line x1="212" y1="1300" x2="242" y2="1300"/>
      </g>
      <text x="208" y="576">850</text><text x="208" y="722">750</text><text x="208" y="868">650</text>
      <text x="208" y="1015">550</text><text x="208" y="1161">450</text><text x="208" y="1307">350</text>
      <text transform="translate(120 915) rotate(-90)" text-anchor="middle" font-size="28" font-weight="500" fill="#1a1f2b">Credit Score</text>
    </g>

    <g class="x-axis" font-size="19" fill="#5f6b7a" text-anchor="middle">
      <line x1="226" y1="1326" x2="2136" y2="1326" stroke="var(--axis)" stroke-width="2.5"/>
      <g stroke="var(--tick)" stroke-width="1.5">
        <line x1="340" y1="1310" x2="340" y2="1340"/><line x1="493" y1="1310" x2="493" y2="1340"/>
        <line x1="645" y1="1310" x2="645" y2="1340"/><line x1="798" y1="1310" x2="798" y2="1340"/>
        <line x1="950" y1="1310" x2="950" y2="1340"/><line x1="1102" y1="1310" x2="1102" y2="1340"/>
        <line x1="1255" y1="1310" x2="1255" y2="1340"/><line x1="1407" y1="1310" x2="1407" y2="1340"/>
        <line x1="1713" y1="1310" x2="1713" y2="1340"/><line x1="1865" y1="1310" x2="1865" y2="1340"/>
        <line x1="2018" y1="1310" x2="2018" y2="1340"/>
      </g>
      <text x="340" y="1370">Jan 2021</text><text x="493" y="1370">Feb 2021</text><text x="645" y="1370">Mar 2021</text>
      <text x="798" y="1370">Apr 2021</text><text x="950" y="1370">May 2021</text><text x="1102" y="1370">Jun 2021</text>
      <text x="1255" y="1370">Jul 2021</text><text x="1407" y="1370">Aug 2021</text><text x="1560" y="1370">Sep 2021</text>
      <text x="1713" y="1370">Oct 2021</text><text x="1865" y="1370">Nov 2021</text><text x="2018" y="1370">Dec 2021</text>
      <text x="1181" y="1460" font-size="28" font-weight="500" fill="#1a1f2b">Credit Pull Date</text>
    </g>

    <line x1="1560" y1="750" x2="1560" y2="1326" stroke="#c4c7cc" stroke-width="1.5"/>
    <circle cx="1560" cy="1326" r="11" fill="var(--header)"/>

    <g class="series" fill="none" stroke-width="4" stroke-linecap="round" transform="translate(0 558.24) scale(1 0.27585)">
      <path vector-effect="non-scaling-stroke" stroke="var(--navy)" d="M226 1137 C300 1165 340 1172 400 1165 C480 1150 540 955 640 955 C720 955 790 1108 865 1108 C940 1108 950 887 1020 887 C1080 885 1120 870 1180 840 C1300 770 1380 686 1470 686 C1510 686 1535 690 1560 697 C1640 720 1680 740 1740 740 C1860 740 1870 637 1920 637 C1980 637 2060 750 2130 780"/>
      <path vector-effect="non-scaling-stroke" stroke="var(--sky)" d="M226 765 C300 800 340 958 400 958 C450 958 470 898 545 898 C700 898 760 1030 875 1030 C1060 1030 1140 937 1240 937 C1300 937 1300 945 1325 945 C1400 945 1440 770 1505 770 C1530 770 1545 785 1560 801 C1630 900 1640 978 1710 978 C1820 978 1860 830 1960 830 C2030 830 2100 885 2135 907"/>
      <path vector-effect="non-scaling-stroke" stroke="var(--teal)" d="M226 1013 C300 960 340 822 400 822 C440 822 480 881 545 881 C700 881 760 748 875 748 C1060 748 1140 842 1240 842 C1300 842 1300 832 1320 832 C1400 832 1440 1008 1505 1008 C1530 1008 1545 995 1560 978 C1640 880 1640 800 1710 800 C1820 800 1860 947 1955 947 C2030 947 2100 890 2135 872"/>
    </g>
    <g fill="#fff" stroke-width="3">
      <circle cx="1560" cy="750" r="11" stroke="var(--navy)"/>
      <circle cx="1560" cy="779" r="11" stroke="var(--sky-deep)"/>
      <circle cx="1560" cy="828" r="11" stroke="var(--teal)"/>
    </g>

    <g class="tooltip" font-size="19">
      <rect x="1462" y="505" width="196" height="160" rx="8" fill="#fff" filter="drop-shadow(0 2px 6px rgba(0,0,0,.08))"/>
      <line x1="1462" y1="546" x2="1658" y2="546" stroke="#e6e8eb" stroke-width="1.5"/>
      <text x="1560" y="533" text-anchor="middle" font-size="17" fill="#1a1f2b">04-02-2022</text>
      <text x="1478" y="579" fill="var(--navy)">Veridian - 725</text>
      <text x="1478" y="611" fill="var(--teal)">Northgate - 695</text>
      <text x="1478" y="645" fill="var(--sky-deep)">Crestline - 706</text>
    </g>
  </svg>
</div>
</body>
</html>
```